Monthly Report PowerPoint Template

We are looking for a set of slides to use as a template for a report that we send out monthly on the state of the solar and storage market. It should be professional and low profile, attached are the slides we currently use/would like to replace: 1) title slide, 2) content summary, 3) content, and 4) section break. We are mainly concerned about a new design for 2), we are using the basic PowerPoint table and would like both a new table style and a version that is more visual. Thanks!

Requirements
Must have
• Light theme
Should not have
• No stock images

```html
<!DOCTYPE html>
<html lang="en">
<head>
<meta charset="utf-8">
<title>Ampere Insight – Monthly Report Slide Template</title>
<link href="https://fonts.googleapis.com/css2?family=Poppins:wght@400;500;600;700&display=swap" rel="stylesheet">
<style>
:root{
  --navy:#1b4a78;
  --navy-dark:#163f68;
  --ink:#333a44;
  --grey-text:#6b7280;
  --rule:#7f9bb8;
  --pale-teal:#e6f2f5;
  --teal:#b9dce4;
  --accent:#f6c66a;
  --accent-line:#f3e6c4;
  --series1:#4a7eb0;
  --series2:#5b9bd5;
  --series3:#a9c4e4;
  --grid:#e3e6ea;
  --cell-grey:#f2f2f2;
  --row-alt:#eeeeee;
}
*{margin:0;padding:0;box-sizing:border-box}
html,body{width:960px;height:1200px;overflow:hidden;background:#fff}
body{position:relative;font-family:'Poppins',sans-serif;color:var(--ink)}
.slide-frame{position:absolute;width:361px;height:203px;box-shadow:0 2px 8px rgba(0,0,0,.12);overflow:hidden;background:#fff}
.slide{position:absolute;left:0;top:0;width:650px;height:366px;transform:scale(.5554);transform-origin:0 0;background:#fff;overflow:hidden}
.pos-1{left:107px;top:58px}.pos-2{left:489px;top:58px}
.pos-3{left:107px;top:277px}.pos-4{left:489px;top:277px}
.pos-5{left:107px;top:497px}.pos-6{left:489px;top:497px}
.pos-7{left:107px;top:716px}.pos-8{left:489px;top:716px}
.pos-9{left:107px;top:935px}
.abs{position:absolute}
.brand{position:absolute;display:flex;align-items:center;gap:3px;color:var(--navy);font-weight:500;white-space:nowrap}
.brand-dot{display:inline-block;border-radius:50%;background:var(--navy)}
.brand-small{right:22px;top:18px;font-size:11px}
.brand-small .brand-dot{width:8px;height:8px}
.footer-rule{position:absolute;left:0;right:30px;top:348px;height:1px;background:var(--accent-line)}
.page-no{position:absolute;right:14px;top:342px;width:14px;height:14px;border-radius:50%;background:var(--navy);color:#fff;font-size:7px;display:flex;align-items:center;justify-content:center}
.slide-title{position:absolute;left:40px;top:28px;font-size:19px;font-weight:400;line-height:23px;color:var(--navy)}
.pill-heading{position:absolute;left:38px;top:28px;height:31px;padding:0 19px;border-radius:16px;background:var(--navy);color:#fff;font-size:18.5px;line-height:31px;white-space:nowrap}
.pill-heading b{font-weight:600}
.body-text{font-size:9px;line-height:11px;color:var(--ink)}
.body-text p{margin-bottom:11px}
.body-text .strong{font-weight:700;color:#222}
.lead{position:absolute;left:40px;font-size:9px;line-height:11px;font-weight:700;color:#222}
/* summary tables */
.summary-table{position:absolute;left:40px;top:80px;width:567px;border-collapse:collapse;font-size:7px;line-height:8.5px}
.summary-table th{text-align:left;font-size:9.5px;font-weight:600;color:#222;padding:8px 5px 6px;border-bottom:1px solid var(--rule)}
.summary-table td{height:40px;padding:0 5px;border-bottom:1px solid var(--rule);vertical-align:middle;color:var(--ink)}
.summary-table td.bullet{padding-left:14px;position:relative}
.summary-table td.bullet::before{content:"";position:absolute;left:5px;top:19px;width:2px;height:2px;border-radius:50%;background:var(--ink)}
.summary-table .col1{width:151px}.summary-table .col2{width:159px}
.summary-table.dark td.lead-cell{background:var(--navy);color:#fff;border-bottom:1px solid #fff}
.summary-table.light th.lead-cell{border:1px solid var(--rule);background:var(--cell-grey)}
.summary-table.light td.lead-cell{background:var(--cell-grey);border:1px solid var(--rule)}
.chart-label{font-family:'Poppins',sans-serif;font-size:7px;fill:var(--grey-text)}
.legend{position:absolute;display:flex;gap:9px;font-size:7px;color:var(--grey-text);white-space:nowrap}
.legend i{display:inline-block;width:5px;height:5px;margin-right:3px;vertical-align:0}
/* data table */
.data-table{position:absolute;left:338px;top:88px;width:277px;border-collapse:collapse;font-size:4.6px;line-height:5.2px;color:var(--ink)}
.data-table th{background:var(--navy);color:#fff;font-weight:600;text-align:left;height:17px;padding:0 5px}
.data-table td{height:18px;padding:0 5px}
.data-table tr:nth-child(even) td{background:var(--row-alt)}
.bullets{list-style:none;font-size:9px;font-weight:700;color:#222;line-height:17px}
.bullets li::before{content:"";display:inline-block;width:4px;height:4px;background:var(--accent);border-radius:50%;margin-right:9px;vertical-align:1px}
</style>
</head>
<body>

<!-- 1 Title -->
<div class="slide-frame pos-1"><section class="slide">
  <svg class="abs" style="left:0;top:0" width="650" height="366" aria-hidden="true">
    <polygon points="465,0 540,0 365,366 290,366" fill="#eef6f8"/>
    <polygon points="540,0 605,0 430,366 365,366" fill="#e2eff3"/>
    <polygon points="605,0 650,0 650,25 478,366 430,366" fill="#f0f7f9"/>
  </svg>
  <div class="brand" style="left:33px;top:42px;font-size:22px;gap:6px"><span class="brand-dot" style="width:18px;height:18px"></span>Ampere Insight</div>
  <h1 class="abs" style="left:33px;top:190px;font-size:35px;font-weight:700;color:var(--navy);line-height:40px">Ampere Insight</h1>
  <div class="abs" style="left:33px;top:250px;height:18px;padding:0 14px;border-radius:9px;background:var(--accent);color:var(--navy);font-size:11px;font-weight:500;line-height:18px">April Update</div>
  <p class="abs" style="left:33px;top:310px;font-size:12.5px;line-height:15px;color:var(--navy)">Residential and<br>Commercial Solar</p>
  <p class="abs" style="left:500px;top:298px;font-size:7.5px;line-height:9px;color:var(--navy)"><b>Some text here</b><br>Some text here Some text here</p>
  <div class="abs" style="left:485px;top:328px;width:157px;height:1px;background:var(--rule)"></div>
  <p class="abs" style="left:500px;top:343px;font-size:7.5px;color:var(--navy)">Some text here Some text here</p>
</section></div>

<!-- 2 Summary dark -->
<div class="slide-frame pos-2"><section class="slide">
  <h2 class="pill-heading">Report Content <b>Summary</b></h2>
  <div class="brand brand-small"><span class="brand-dot"></span>Ampere Insight</div>
  <table class="summary-table dark">
    <tr><th class="col1">Text here</th><th class="col2">Text here</th><th>Text here</th></tr>
    <tr><td class="lead-cell">Nunc viverra imperdiet enim. Fusce est. Vivamus a tellus.</td><td class="bullet">Nunc viverra imperdiet enim. Fusce est. Vivamus a tellus.</td><td class="bullet">Nunc viverra imperdiet enim. Fusce est. Vivamus a tellus.</td></tr>
    <tr><td class="lead-cell">Nunc viverra imperdiet enim. Fusce est. Vivamus a tellus.</td><td class="bullet">Nunc viverra imperdiet enim. Fusce est. Vivamus a tellus.</td><td class="bullet">Nunc viverra imperdiet enim. Fusce est. Vivamus a tellus.</td></tr>
    <tr><td class="lead-cell">Nunc viverra imperdiet enim. Fusce est. Vivamus a tellus.</td><td class="bullet">Nunc viverra imperdiet enim. Fusce est. Vivamus a tellus.</td><td class="bullet">Nunc viverra imperdiet enim. Fusce est. Vivamus a tellus.</td></tr>
    <tr><td class="lead-cell">Nunc viverra imperdiet enim. Fusce est. Vivamus a tellus.</td><td class="bullet">Nunc viverra imperdiet enim. Fusce est. Vivamus a tellus.</td><td class="bullet">Nunc viverra imperdiet enim. Fusce est. Vivamus a tellus.</td></tr>
    <tr><td class="lead-cell">Nunc viverra imperdiet enim. Fusce est. Vivamus a tellus.</td><td class="bullet">Nunc viverra imperdiet enim. Fusce est. Vivamus a tellus.</td><td class="bullet">Nunc viverra imperdiet enim. Fusce est. Vivamus a tellus.</td></tr>
  </table>
  <div class="footer-rule"></div><div class="page-no">2</div>
</section></div>

<!-- 3 Summary light -->
<div class="slide-frame pos-3"><section class="slide">
  <h2 class="pill-heading">Report Content <b>Summary</b></h2>
  <div class="brand brand-small"><span class="brand-dot"></span>Ampere Insight</div>
  <table class="summary-table light">
    <tr><th class="col1 lead-cell">Text here</th><th class="col2">Text here</th><th>Text here</th></tr>
    <tr><td class="lead-cell">Nunc viverra imperdiet enim. Fusce est. Vivamus a tellus.</td><td class="bullet">Nunc viverra imperdiet enim. Fusce est. Vivamus a tellus.</td><td class="bullet">Nunc viverra imperdiet enim. Fusce est. Vivamus a tellus.</td></tr>
    <tr><td class="lead-cell">Nunc viverra imperdiet enim. Fusce est. Vivamus a tellus.</td><td class="bullet">Nunc viverra imperdiet enim. Fusce est. Vivamus a tellus.</td><td class="bullet">Nunc viverra imperdiet enim. Fusce est. Vivamus a tellus.</td></tr>
    <tr><td class="lead-cell">Nunc viverra imperdiet enim. Fusce est. Vivamus a tellus.</td><td class="bullet">Nunc viverra imperdiet enim. Fusce est. Vivamus a tellus.</td><td class="bullet">Nunc viverra imperdiet enim. Fusce est. Vivamus a tellus.</td></tr>
    <tr><td class="lead-cell">Nunc viverra imperdiet enim. Fusce est. Vivamus a tellus.</td><td class="bullet">Nunc viverra imperdiet enim. Fusce est. Vivamus a tellus.</td><td class="bullet">Nunc viverra imperdiet enim. Fusce est. Vivamus a tellus.</td></tr>
    <tr><td class="lead-cell">Nunc viverra imperdiet enim. Fusce est. Vivamus a tellus.</td><td class="bullet">Nunc viverra imperdiet enim. Fusce est. Vivamus a tellus.</td><td class="bullet">Nunc viverra imperdiet enim. Fusce est. Vivamus a tellus.</td></tr>
  </table>
  <div class="footer-rule"></div><div class="page-no">3</div>
</section></div>

<!-- 4 Section break -->
<div class="slide-frame pos-4"><section class="slide" style="background:linear-gradient(215deg,#ffffff 0%,#e4f1f4 35%,var(--teal) 100%)">
  <div class="brand brand-small"><span class="brand-dot"></span>Ampere Insight</div>
  <h2 class="abs" style="left:48px;top:228px;font-size:29px;line-height:36px;font-weight:700;color:var(--navy)">Residential Solar:<br>Market Demand Trends</h2>
  <div class="footer-rule" style="background:rgba(255,255,255,.5)"></div><div class="page-no">4</div>
</section></div>

<!-- 5 Text + chart -->
<div class="slide-frame pos-5"><section class="slide">
  <h2 class="slide-title">Monthly Residential Permits<br>Issued Trends</h2>
  <div class="brand brand-small"><span class="brand-dot"></span>Ampere Insight</div>
  <div class="abs body-text" style="left:40px;top:104px;width:272px">
    <p>Lorem ipsum dolor sit amet, consectetuer adipiscing elit. Maecenas porttitor congue massa. Fusce posuere, magna sed pulvinar ultricies, purus lectus malesuada libero, sit amet commodo magna eros quis urna.</p>
    <p>Nunc viverra imperdiet enim. Fusce est. Vivamus a tellus.</p>
    <p style="margin-bottom:26px">Pellentesque habitant morbi tristique senectus et netus et malesuada fames ac turpis egestas. Proin pharetra nonummy pede. Mauris et orci.<br>Nunc viverra imperdiet enim. Fusce est. Vivamus a tellus.</p>
    <p class="strong">Lorem ipsum dolor sit amet, consectetuer adipiscing elit. Maecenas porttitor congue massa. Fusce posuere, magna sed pulvinar ultricies, purus lectus malesuada libero, sit amet commod</p>
  </div>
  <svg class="abs" style="left:318px;top:100px" width="310" height="170" aria-label="Clustered bar chart of permits by category">
    <g stroke="var(--grid)" stroke-width="1">
      <line x1="30" y1="150" x2="295" y2="150"/><line x1="30" y1="130" x2="295" y2="130"/><line x1="30" y1="110" x2="295" y2="110"/><line x1="30" y1="90" x2="295" y2="90"/><line x1="30" y1="70" x2="295" y2="70"/><line x1="30" y1="50" x2="295" y2="50"/><line x1="30" y1="30" x2="295" y2="30"/>
    </g>
    <g class="chart-label" text-anchor="end"><text x="22" y="153">0</text><text x="22" y="133">1</text><text x="22" y="113">2</text><text x="22" y="93">3</text><text x="22" y="73">4</text><text x="22" y="53">5</text><text x="22" y="33">6</text></g>
    <g transform="translate(0,-20)">
      <rect x="43" y="84" width="11" height="86" fill="var(--series1)"/><rect x="56" y="122" width="11" height="48" fill="var(--series2)"/><rect x="69" y="130" width="11" height="40" fill="var(--series3)"/>
      <rect x="108" y="120" width="11" height="50" fill="var(--series1)"/><rect x="121" y="82" width="11" height="88" fill="var(--series2)"/><rect x="134" y="130" width="11" height="40" fill="var(--series3)"/>
      <rect x="173" y="100" width="11" height="70" fill="var(--series1)"/><rect x="186" y="134" width="11" height="36" fill="var(--series2)"/><rect x="199" y="110" width="11" height="60" fill="var(--series3)"/>
      <rect x="238" y="80" width="11" height="90" fill="var(--series1)"/><rect x="251" y="114" width="11" height="56" fill="var(--series2)"/><rect x="264" y="70" width="11" height="100" fill="var(--series3)"/>
    </g>
    <g class="chart-label" text-anchor="middle"><text x="62" y="164">Category 1</text><text x="127" y="164">Category 2</text><text x="192" y="164">Category 3</text><text x="257" y="164">Category 4</text></g>
  </svg>
  <div class="legend" style="left:394px;top:279px"><span><i style="background:var(--series1)"></i>Series 1</span><span><i style="background:var(--series2)"></i>Series 2</span><span><i style="background:var(--series3)"></i>Series 3</span></div>
  <div class="footer-rule"></div><div class="page-no">5</div>
</section></div>

<!-- 6 Wide chart -->
<div class="slide-frame pos-6"><section class="slide">
  <h2 class="slide-title">Monthly Residential Permits<br>Issued Trends</h2>
  <div class="brand brand-small"><span class="brand-dot"></span>Ampere Insight</div>
  <p class="lead" style="top:88px;width:570px">Lorem ipsum dolor sit amet, consectetuer adipiscing elit. Maecenas porttitor congue massa. Fusce posuere, magna sed pulvinar ultricies, purus lectus malesuada libero, sit amet commod</p>
  <svg class="abs" style="left:25px;top:140px" width="600" height="140" aria-label="Clustered bar chart of permits by category">
    <g stroke="var(--grid)" stroke-width="1">
      <line x1="30" y1="127" x2="595" y2="127"/><line x1="30" y1="108" x2="595" y2="108"/><line x1="30" y1="89" x2="595" y2="89"/><line x1="30" y1="70" x2="595" y2="70"/><line x1="30" y1="51" x2="595" y2="51"/><line x1="30" y1="32" x2="595" y2="32"/><line x1="30" y1="13" x2="595" y2="13"/>
    </g>
    <g class="chart-label" text-anchor="end"><text x="22" y="130">0</text><text x="22" y="111">1</text><text x="22" y="92">2</text><text x="22" y="73">3</text><text x="22" y="54">4</text><text x="22" y="35">5</text><text x="22" y="16">6</text></g>
    <rect x="63" y="45" width="22" height="82" fill="var(--series1)"/><rect x="91" y="82" width="22" height="45" fill="var(--series2)"/><rect x="119" y="89" width="22" height="38" fill="var(--series3)"/>
    <rect x="200" y="80" width="22" height="47" fill="var(--series1)"/><rect x="228" y="43" width="22" height="84" fill="var(--series2)"/><rect x="256" y="89" width="22" height="38" fill="var(--series3)"/>
    <rect x="338" y="60" width="22" height="67" fill="var(--series1)"/><rect x="366" y="93" width="22" height="34" fill="var(--series2)"/><rect x="394" y="70" width="22" height="57" fill="var(--series3)"/>
    <rect x="476" y="42" width="22" height="85" fill="var(--series1)"/><rect x="504" y="74" width="22" height="53" fill="var(--series2)"/><rect x="532" y="32" width="22" height="95" fill="var(--series3)"/>
  </svg>
  <div class="abs" style="left:25px;top:270px;width:600px;font-size:7px;color:var(--grey-text)">
    <span class="abs" style="left:78px">Category 1</span><span class="abs" style="left:215px">Category 2</span><span class="abs" style="left:353px">Category 3</span><span class="abs" style="left:491px">Category 4</span>
  </div>
  <div class="legend" style="left:271px;top:287px"><span><i style="background:var(--series1)"></i>Series 1</span><span><i style="background:var(--series2)"></i>Series 2</span><span><i style="background:var(--series3)"></i>Series 3</span></div>
  <div class="footer-rule"></div><div class="page-no">6</div>
</section></div>

<!-- 7 Donuts -->
<div class="slide-frame pos-7"><section class="slide">
  <h2 class="slide-title">Monthly Residential Permits<br>Issued Trends</h2>
  <div class="brand brand-small"><span class="brand-dot"></span>Ampere Insight</div>
  <p class="lead" style="top:88px;width:570px">Lorem ipsum dolor sit amet, consectetuer adipiscing elit. Maecenas porttitor congue massa. Fusce posuere, magna sed pulvinar ultricies, purus lectus malesuada libero, sit amet commod</p>
  <svg class="abs" style="left:0;top:140px" width="650" height="160" aria-label="Three donut charts of quarterly share">
    <g fill="none" stroke-width="25">
      <g transform="translate(143,80) rotate(-90)">
        <circle r="57" stroke="var(--series1)" stroke-dasharray="197 161"/>
        <circle r="57" stroke="var(--series2)" stroke-dasharray="90 268" stroke-dashoffset="-197"/>
        <circle r="57" stroke="var(--series3)" stroke-dasharray="71 287" stroke-dashoffset="-287"/>
      </g>
      <g transform="translate(322,80) rotate(-90)">
        <circle r="57" stroke="#cbcbcb" stroke-dasharray="197 161"/>
        <circle r="57" stroke="#a5a5a5" stroke-dasharray="90 268" stroke-dashoffset="-197"/>
        <circle r="57" stroke="#8a8a8a" stroke-dasharray="71 287" stroke-dashoffset="-287"/>
      </g>
      <g transform="translate(510,80) rotate(-90)">
        <circle r="57" stroke="#fdd9a0" stroke-dasharray="197 161"/>
        <circle r="57" stroke="#fdc20a" stroke-dasharray="90 268" stroke-dashoffset="-197"/>
        <circle r="57" stroke="#cf9a00" stroke-dasharray="71 287" stroke-dashoffset="-287"/>
      </g>
    </g>
  </svg>
  <div class="legend" style="left:84px;top:298px"><span><i style="background:var(--series1)"></i>2nd Qtr</span><span><i style="background:var(--series2)"></i>3rd Qtr</span><span><i style="background:var(--series3)"></i>4th Qtr</span></div>
  <div class="legend" style="left:264px;top:298px"><span><i style="background:#cbcbcb"></i>2nd Qtr</span><span><i style="background:#a5a5a5"></i>3rd Qtr</span><span><i style="background:#8a8a8a"></i>4th Qtr</span></div>
  <div class="legend" style="left:451px;top:298px"><span><i style="background:#fdd9a0"></i>2nd Qtr</span><span><i style="background:#fdc20a"></i>3rd Qtr</span><span><i style="background:#cf9a00"></i>4th Qtr</span></div>
  <div class="footer-rule"></div><div class="page-no">7</div>
</section></div>

<!-- 8 Two columns -->
<div class="slide-frame pos-8"><section class="slide">
  <h2 class="slide-title">Monthly Residential Permits<br>Issued Trends</h2>
  <div class="brand brand-small"><span class="brand-dot"></span>Ampere Insight</div>
  <div class="abs body-text" style="left:40px;top:104px;width:272px">
    <p>Lorem ipsum dolor sit amet, consectetuer adipiscing elit. Maecenas porttitor congue massa. Fusce posuere, magna sed pulvinar ultricies, purus lectus malesuada libero, sit amet commodo magna eros quis urna.</p>
    <p>Nunc viverra imperdiet enim. Fusce est. Vivamus a tellus.</p>
    <p style="margin-bottom:26px">Pellentesque habitant morbi tristique senectus et netus et malesuada fames ac turpis egestas. Proin pharetra nonummy pede. Mauris et orci.<br>Nunc viverra imperdiet enim. Fusce est. Vivamus a tellus.</p>
    <p class="strong">Lorem ipsum dolor sit amet, consectetuer adipiscing elit. Maecenas porttitor congue massa. Fusce posuere, magna sed pulvinar ultricies, purus lectus malesuada libero, sit amet commod</p>
  </div>
  <div class="abs body-text" style="left:342px;top:104px;width:268px">
    <p>Lorem ipsum dolor sit amet, consectetuer adipiscing elit. Maecenas porttitor congue massa. Fusce posuere, magna sed pulvinar ultricies, purus lectus malesuada libero, sit amet commodo magna eros quis urna.</p>
    <p>Nunc viverra imperdiet enim. Fusce est. Vivamus a tellus.</p>
    <p>Pellentesque habitant morbi tristique senectus et netus et malesuada fames ac turpis egestas. Proin pharetra nonummy pede. Mauris et orci. Pellentesque habitant morbi tristique senectus et netus et malesuada fames ac turpis egestas. Proin pharetra nonummy pede. Mauris et orci.</p>
    <p>Nunc viverra imperdiet enim. Fusce est. Vivamus a tellus<br>Nunc viverra imperdiet enim. Fusce est. Vivamus a tellus.</p>
  </div>
  <div class="footer-rule"></div><div class="page-no">8</div>
</section></div>

<!-- 9 Text + data table -->
<div class="slide-frame pos-9"><section class="slide">
  <h2 class="slide-title">Monthly Residential Permits<br>Issued Trends</h2>
  <div class="brand brand-small"><span class="brand-dot"></span>Ampere Insight</div>
  <div class="abs body-text" style="left:40px;top:84px;width:272px">
    <p>Lorem ipsum dolor sit amet, consectetuer adipiscing elit. Maecenas porttitor congue massa. Fusce posuere, magna sed pulvinar ultricies, purus lectus malesuada libero, sit amet commodo magna eros quis urna.</p>
    <p>Nunc viverra imperdiet enim. Fusce est. Vivamus a tellus.</p>
    <p>Pellentesque habitant morbi tristique senectus et netus et malesuada fames ac turpis egestas. Proin pharetra nonummy pede. Mauris et orci.</p>
    <p style="margin-bottom:10px">Nunc viverra imperdiet enim. Fusce est. Vivamus a tellus.</p>
    <ul class="bullets"><li>Lorem ipsum dolor sit amet,</li><li>adipiscing elit. Maecenas</li><li>Fusce posuere, magna sed pu</li></ul>
  </div>
  <table class="data-table">
    <tr><th style="width:95px">Text here</th><th style="width:56px">Text here</th><th>Text here</th></tr>
    <tr><td>Nunc viverra imperdiet</td><td>00000000</td><td>Nunc viverra imperdiet enim. Fusce est. Vivamus a tellus.</td></tr>
    <tr><td>Nunc viverra imperdiet</td><td>00000000</td><td>Nunc viverra imperdiet enim. Fusce est. Vivamus a tellus.</td></tr>
    <tr><td>Nunc viverra imperdiet</td><td>00000000</td><td>Nunc viverra imperdiet enim. Fusce est. Vivamus a tellus.</td></tr>
    <tr><td>Nunc viverra imperdiet</td><td>00000000</td><td>Nunc viverra imperdiet enim. Fusce est. Vivamus a tellus.</td></tr>
    <tr><td>Nunc viverra imperdiet</td><td>00000000</td><td>Nunc viverra imperdiet enim. Fusce est. Vivamus a tellus.</td></tr>
    <tr><td>Nunc viverra imperdiet</td><td>00000000</td><td>Nunc viverra imperdiet enim. Fusce est. Vivamus a tellus.</td></tr>
    <tr><td>Nunc viverra imperdiet</td><td>00000000</td><td>Nunc viverra imperdiet enim. Fusce est. Vivamus a tellus.</td></tr>
    <tr><td>Nunc viverra imperdiet</td><td>00000000</td><td>Nunc viverra imperdiet enim. Fusce est. Vivamus a tellus.</td></tr>
    <tr><td>Nunc viverra imperdiet</td><td>00000000</td><td>Nunc viverra imperdiet enim. Fusce est. Vivamus a tellus.</td></tr>
    <tr><td>Nunc viverra imperdiet</td><td>00000000</td><td>Nunc viverra imperdiet enim. Fusce est. Vivamus a tellus.</td></tr>
  </table>
  <p class="abs body-text" style="left:40px;top:307px;width:575px">Lorem ipsum dolor sit amet, consectetuer adipiscing elit. Maecenas porttitor congue massa. Fusce posuere, magna sed pulvinar ultricies, purus lectus malesuada libero, sit amet commod</p>
  <div class="footer-rule"></div><div class="page-no">9</div>
</section></div>

</body>
</html>
```